2 Page Website in "wordpress"

We just bought rigadvisorhub.example and we need a 2 page website in wordpress coding. The top of the page should have a place to flash pictures of equipment examples that we consult on, selling or buying. "you can borrow pictures of all kinds of Dozers, Excavators, Backhoes, Mining Equipment from all over the Internet.

THE HOME PAGE
Then the first page needs to have 2 sections for general content, with links menu built in somewhere. We may add up to 10-15 links over time, so save some space for us. Then the 2nd page just needs to be a general contact form, for the buyer and seller. The 2 sections need to be set up for. 1.The buyer - Explanation - 2. For the Seller - Explanation -

THE FORM PAGE
There will be about 10 fields for general info so they can submit inquries, whether it is a seller contacting us to sell equipment, or a buyer wanting us to find them a specific piece of equipment. Just figure about 10 fields.

Logo
We need logo built in that represents equipment sales….

THIS MUST BE BUILT IN WORDPRESS CODE. It is our understanding that google is favoring websites built in wordpress.

Industry/Entity Type

Internet

Requirements
Must have
• Wordpress coded

```html
<!DOCTYPE html>
<html lang="en">
<head>
<meta charset="utf-8">
<title>Rig Advisor Hub</title>
<link href="https://fonts.googleapis.com/css2?family=Open+Sans:wght@400;600&display=swap" rel="stylesheet">
<style>
:root{
  --orange:#e5870a;
  --orange-dark:#c76f05;
  --text:#555;
  --nav:#666;
  --field:#ececec;
  --field-border:#ddd;
  --grey-btn:#7a7a7a;
  --footer:#2f2f2f;
  --white:#fff;
}
*{margin:0;padding:0;box-sizing:border-box}
html,body{width:1200px;height:1200px;overflow:hidden;background:var(--white);font-family:'Open Sans',sans-serif}
.site{position:relative;width:1200px;height:1200px}

.site-header{position:absolute;top:0;left:0;width:1200px;height:100px}
.brand{position:absolute;left:100px;top:24px;display:flex;align-items:center;gap:14px}
.brand-mark{width:40px;height:40px;border-radius:50%;background:var(--orange)}
.brand-name{font-size:23px;line-height:27px;color:var(--orange);font-weight:400;width:140px}
.main-nav{position:absolute;top:32px;right:99px;display:flex;align-items:center;font-size:14px}
.main-nav a{color:var(--nav);text-decoration:none;margin-left:43px}
.main-nav .is-current{border:1px solid var(--orange);color:var(--orange);font-weight:600;padding:4px 18px;border-radius:2px;margin-left:0}
.main-nav .nav-contact{background:var(--orange);color:var(--white);padding:7px 42px 8px;border-bottom:4px solid var(--orange-dark);border-radius:3px;margin-left:28px}

.hero{position:absolute;top:100px;left:0;width:1200px;height:670px;
  background:linear-gradient(180deg,#4d4d47 0%,#6b6456 35%,#5b4d36 60%,#4a4137 100%)}
.hero-photo{position:absolute;inset:0;
  background:radial-gradient(ellipse 330px 300px at 400px 320px,rgba(214,160,30,.55),rgba(0,0,0,0) 70%)}
.hero-arrow{position:absolute;top:313px;width:38px;height:38px}
.hero-arrow.prev{left:27px}
.hero-arrow.next{right:29px}

.inquiry{position:absolute;left:690px;top:252px;width:412px;height:373px;background:var(--white)}
.inquiry-tabs{display:flex;height:53px}
.inquiry-tabs span{flex:1;display:flex;align-items:center;justify-content:center;font-size:16px;font-weight:600;color:var(--orange)}
.inquiry-tabs .tab-active{background:var(--orange);color:var(--white)}
.inquiry-form{padding:38px 31px 0 30px}
.field{display:flex;align-items:center;height:34px;margin-bottom:6px}
.field label{width:102px;font-size:13px;line-height:15px;color:var(--text)}
.field span{flex:1;height:34px;background:var(--field);border:1px solid var(--field-border)}
.submit{display:block;margin:18px 0 0 auto;width:122px;height:34px;background:var(--orange);border-bottom:4px solid var(--orange-dark);color:var(--white);font-size:13px;text-align:center;line-height:31px}

.intro{position:absolute;top:818px;left:100px;width:1000px}
.intro h1{font-size:30px;font-weight:400;color:var(--orange);line-height:40px}
.intro-copy{position:absolute;top:56px;left:-1px;width:726px;font-size:13px;line-height:18px;color:var(--text);text-align:justify}
.intro-copy p{margin-bottom:18px}
.quick-links{position:absolute;top:60px;left:765px;width:236px}
.quick-links a{display:block;height:41px;margin-bottom:10px;background:var(--grey-btn);color:var(--white);font-size:18px;font-weight:600;text-align:center;line-height:40px;text-decoration:none}
.quick-links .link-primary{background:var(--orange);border-bottom:3px solid var(--orange-dark)}

.site-footer{position:absolute;top:1106px;left:0;width:1200px;height:94px;background:var(--footer);color:var(--white);font-size:13px;text-align:center}
.footer-meta{padding-top:22px}
.footer-meta .sep{margin:0 8px}
.social{display:flex;justify-content:center;gap:14px;margin-top:12px}
.social span{width:10px;height:10px;border-radius:50%;background:var(--white)}
</style>
</head>
<body>
<div class="site">
  <header class="site-header">
    <div class="brand">
      <span class="brand-mark"></span>
      <span class="brand-name">Rig Advisor Hub</span>
    </div>
    <nav class="main-nav">
      <a class="is-current">Home</a>
      <a>About Us</a>
      <a>Service</a>
      <a>Blog</a>
      <a class="nav-contact">Contact</a>
    </nav>
  </header>

  <section class="hero">
    <div class="hero-photo" role="img" aria-label="Yellow tracked excavator on a dirt site under a stormy sky"></div>
    <svg class="hero-arrow prev" viewBox="0 0 38 38" aria-hidden="true"><circle cx="19" cy="19" r="17.5" fill="none" stroke="#9a9a9a" stroke-width="2"/><path d="M27 19H12M18 12l-7 7 7 7" fill="none" stroke="#9a9a9a" stroke-width="3"/></svg>
    <svg class="hero-arrow next" viewBox="0 0 38 38" aria-hidden="true"><circle cx="19" cy="19" r="17.5" fill="none" stroke="#9a9a9a" stroke-width="2"/><path d="M11 19h15M20 12l7 7-7 7" fill="none" stroke="#9a9a9a" stroke-width="3"/></svg>

    <div class="inquiry">
      <div class="inquiry-tabs">
        <span>Are you a Buyer ?</span>
        <span class="tab-active">Are you a Seller ?</span>
      </div>
      <div class="inquiry-form">
        <div class="field"><label>Name:</label><span></span></div>
        <div class="field"><label>Number:</label><span></span></div>
        <div class="field"><label>Equipment Needed:</label><span></span></div>
        <div class="field"><label>Quantity:</label><span></span></div>
        <div class="field"><label>Location:</label><span></span></div>
        <span class="submit">SUBMIT</span>
      </div>
    </div>
  </section>

  <section class="intro">
    <h1>Welcome To Rig Advisor Hub</h1>
    <div class="intro-copy">
      <p>Lorem ipsum dolor sit amet, consectetur adipiscing elit. Nullam pretium ullamcorper lorem ut suscipit. Nullam at ornare mi. Cras volutpat dictum rhoncus. Phasellus sed nisl tincidunt, rutrum diam sit amet, scelerisque arcu. Integer vehiculaa felis tempor urna fermentum, vulputate lobortis risus ultrices. Nam mi nulla, aliquam ac pellentesque sit amet, lobortis eu ligula. Cras vel ex porta urna egestas hendrerit in eu sapien.</p>
      <p>Donec quis libero sed justo suscipit lacinia. Nam vulputate feugiat ante. Pellentesque lorem libero, viverra in sapien in, tincidunt pulvinar tortor. Nulla pellentesque turpis sit amet augue mollis malesuada. Curabitur ut nisl a elit interdum imperdiet. Donec feugiat id nunc id sollicitudin. In lacinia commodo velit.</p>
    </div>
    <nav class="quick-links">
      <a class="link-primary">Reviews</a>
      <a>reports</a>
      <a>More</a>
    </nav>
  </section>

  <footer class="site-footer">
    <div class="footer-meta">© 2014 yoursite all rights reserved <span class="sep">|</span> Privacy <span class="sep">|</span>Terms &amp; Conditions</div>
    <div class="social"><span></span><span></span><span></span></div>
  </footer>
</div>
</body>
</html>
```